Willowmere Counseling (Endure - Mend - Flourish) - Double Sided Business Card

I would like a 2-sided business card. Front: Matte Black or Navy with Logo & Tagline. Back: Name, Address, Phone Number, Email, & Website (maybe would like to include a small map pin-pointing location); Prefer front to be a gold/silver foil (iridescent); Back prefer white or light colored background with lettering that is easy to read and simple

Target Market(s)

Individuals & Couples (13 y.o. - ALL Adults); High end clientele

Industry/Entity Type

Licensed Professional Counselor (Mental Health)

Contact Information for Business Card

Name: Willowmere Counseling; Tagline: Endure - Mend - Flourish; Address: 3870 N. Garrick Ave., Suite 214, Fort Worth, TX 76132; Phone: (214) 555-0187; Website: www.WillowmereCounseling.example

Font styles to use
Serif

Requirements
Must have
• Logo on Front (Large) prefer gold/silver foil on a matte dark color (i.e. black, navy, etc.); Back of Card: All other relevant information

```html
<!DOCTYPE html>
<html lang="en">
<head>
<meta charset="utf-8">
<title>Willowmere Counseling – Business Card</title>
<link href="https://fonts.googleapis.com/css2?family=Cinzel:wght@400;600&family=Lora:wght@400&display=swap" rel="stylesheet">
<style>
  :root {
    --backdrop: #5a5a5c;
    --card-dark: #1b1b1c;
    --card-frame: #1e1e22;
    --gold: #d8b95b;
    --silver: #8a8a8c;
    --ink: #1e1e22;
  }
  html, body {
    margin: 0;
    padding: 0;
    width: 1200px;
    height: 1195px;
    overflow: hidden;
    background: var(--backdrop);
  }
  .canvas {
    position: relative;
    width: 1200px;
    height: 1195px;
  }
  .card {
    position: absolute;
    left: 237px;
    width: 726px;
    height: 440px;
    box-sizing: border-box;
  }
  .card-front {
    top: 137px;
    background: var(--card-dark);
    display: flex;
    flex-direction: column;
    align-items: center;
    justify-content: center;
  }
  .brand-mark {
    width: 94px;
    height: 94px;
    border-radius: 50%;
    border: 2px solid var(--gold);
    box-sizing: border-box;
    margin-bottom: 12px;
  }
  .brand-name {
    font-family: "Cinzel", serif;
    font-weight: 600;
    color: var(--gold);
    font-size: 40px;
    line-height: 1;
    letter-spacing: 0.5px;
    margin: 0;
    text-align: center;
  }
  .brand-sub {
    display: flex;
    align-items: center;
    gap: 6px;
    margin-top: 4px;
  }
  .brand-sub .rule {
    width: 58px;
    height: 2px;
    background: var(--silver);
  }
  .brand-sub span {
    font-family: "Cinzel", serif;
    color: var(--silver);
    font-size: 20px;
    letter-spacing: 5px;
  }
  .tagline {
    font-family: "Cinzel", serif;
    color: var(--gold);
    font-size: 13.5px;
    margin-top: 4px;
    letter-spacing: 0.3px;
  }
  .card-back {
    top: 618px;
    background: var(--gold);
    border: 21px solid var(--card-frame);
    padding: 0 0 0 76px;
  }
  .back-title {
    font-family: "Cinzel", serif;
    color: var(--ink);
    font-size: 26px;
    letter-spacing: 5px;
    margin: 82px 0 0;
    font-weight: 400;
  }
  .contact-list {
    list-style: none;
    margin: 108px 0 0;
    padding: 0;
  }
  .contact-list li {
    display: flex;
    align-items: center;
    gap: 12px;
    height: 31px;
    font-family: "Lora", serif;
    font-size: 14px;
    color: var(--ink);
  }
  .contact-list svg {
    width: 22px;
    height: 22px;
    flex: none;
  }
</style>
</head>
<body>
<main class="canvas">
  <section class="card card-front" aria-label="Card front">
    <div class="brand-mark" aria-hidden="true"></div>
    <h1 class="brand-name">WILLOWMERE</h1>
    <div class="brand-sub"><i class="rule"></i><span>COUNSELING</span><i class="rule"></i></div>
    <p class="tagline">ENDURE - MEND - FLOURISH</p>
  </section>

  <section class="card card-back" aria-label="Card back">
    <h2 class="back-title">WILLOWMERE COUNSELING</h2>
    <ul class="contact-list">
      <li>
        <svg viewBox="0 0 24 24" aria-hidden="true"><path fill="#1e1e22" d="M12 2a7 7 0 0 0-7 7c0 5 7 13 7 13s7-8 7-13a7 7 0 0 0-7-7zm0 9.5A2.5 2.5 0 1 1 12 6.5a2.5 2.5 0 0 1 0 5z"/></svg>
        3870 N. Garrick Ave., Suite 214, Fort Worth, TX 76132
      </li>
      <li>
        <svg viewBox="0 0 24 24" aria-hidden="true"><path fill="#1e1e22" d="M6.6 10.8a15 15 0 0 0 6.6 6.6l2.2-2.2a1 1 0 0 1 1-.25 11.4 11.4 0 0 0 3.6.57 1 1 0 0 1 1 1V20a1 1 0 0 1-1 1A17 17 0 0 1 3 4a1 1 0 0 1 1-1h3.5a1 1 0 0 1 1 1c0 1.25.2 2.45.57 3.57a1 1 0 0 1-.25 1z"/><path fill="none" stroke="#1e1e22" stroke-width="1.6" d="M14 3.5a7 7 0 0 1 6.5 6.5M14 7a3.5 3.5 0 0 1 3 3"/></svg>
        (214) 555-0187
      </li>
      <li>
        <svg viewBox="0 0 24 24" aria-hidden="true"><g fill="none" stroke="#1e1e22" stroke-width="1.6"><circle cx="12" cy="12" r="10"/><ellipse cx="12" cy="12" rx="4.5" ry="10"/><path d="M2 12h20M12 2v20"/></g></svg>
        www.WillowmereCounseling.example
      </li>
    </ul>
  </section>
</main>
</body>
</html>
```